Business Card and Simple Logo Desgin

New Zealand based start up company "Brava Advisory LTD" requires business cards and simple logo design.

Card Content.

Brava Advisory LTD

Rosalind Kettering
CA, BMS (Hons)

r.kettering@bravaadvisory.example.nz
PH +64 21 705 146

Target Market(s)

Corporate Business in IT, Finance and accounting.

Industry/Entity Type

Business

```html
<!DOCTYPE html>
<html lang="en">
<head>
<meta charset="utf-8">
<title>Brava Advisory LTD — Business Card</title>
<link rel="stylesheet" href="https://fonts.googleapis.com/css2?family=Bebas+Neue&family=Roboto:wght@400&family=Roboto+Condensed:wght@400&display=swap">
<style>
  :root {
    --page-bg: #ffffff;
    --card-bg: #f1f1f1;
    --ink: #111111;
    --pattern-dark: #2b2b2b;
    --pattern-light: #6a6a6a;
  }
  html, body {
    margin: 0;
    padding: 0;
    width: 900px;
    height: 1200px;
    overflow: hidden;
    background: var(--page-bg);
  }
  .business-card {
    position: absolute;
    left: 152px;
    top: 107px;
    width: 576px;
    height: 1006px;
    background: var(--card-bg);
    color: var(--ink);
  }
  .pattern-band {
    position: absolute;
    left: 0;
    top: 0;
    width: 100%;
    height: 351px;
    background: linear-gradient(180deg, var(--pattern-light) 0%, var(--pattern-dark) 100%);
  }
  .company-name {
    position: absolute;
    left: 58px;
    top: 446px;
    margin: 0;
    font-family: "Bebas Neue", "Oswald", sans-serif;
    font-weight: 400;
    font-size: 80px;
    line-height: 80px;
    letter-spacing: 0.5px;
    text-transform: uppercase;
  }
  .company-name span { display: block; }
  .contact {
    position: absolute;
    left: 58px;
    top: 770px;
  }
  .contact-name {
    margin: 0;
    font-family: "Roboto Condensed", "Arial Narrow", sans-serif;
    font-size: 31px;
    line-height: 36px;
  }
  .contact-credentials {
    margin: 2px 0 0;
    font-family: "Roboto Condensed", "Arial Narrow", sans-serif;
    font-size: 18px;
    line-height: 22px;
  }
  .contact-email {
    margin: 20px 0 0;
    font-family: "Roboto", Arial, sans-serif;
    font-size: 27px;
    line-height: 34px;
    letter-spacing: -0.3px;
  }
  .contact-phone {
    margin: 4px 0 0;
    font-family: "Roboto", Arial, sans-serif;
    font-size: 29px;
    line-height: 36px;
  }
  .contact-phone .label {
    font-size: 17px;
    margin-right: 6px;
  }
</style>
</head>
<body>
  <article class="business-card">
    <div class="pattern-band" role="img" aria-label="Black and white interlocking woven geometric pattern"></div>

    <h1 class="company-name">
      <span>Brava</span>
      <span>Advisory</span>
      <span>LTD</span>
    </h1>

    <address class="contact" style="font-style: normal;">
      <p class="contact-name">Rosalind Kettering</p>
      <p class="contact-credentials">CA, BMS (Hons)</p>
      <p class="contact-email">r.kettering@bravaadvisory.example.nz</p>
      <p class="contact-phone"><span class="label">Tel</span>+64 21 705 146</p>
    </address>
  </article>
</body>
</html>
```